Season Greeting Card

We need an email Season Greeting card to send at year end. It should be NOT religious or refer to any religion. We want to have this graphic in the body of a year-end greetings email.

The theme should be Australian or non-specific. The company is in Perth, Western Australia. I want to have space to add a company logo and space to insert some personal text.

I will attach some previous versions. They are NOT what I want to see in the new version. They are JPG which is NOT the form I expect to see. They are un-imaginative, boring and too European. However, they do contain the essential elements of company name and specific text.

Target Market(s)

Business clients

Industry/Entity Type

Religious

```html
<!DOCTYPE html>
<html lang="en">
<head>
<meta charset="utf-8">
<title>Season's Greetings – Marlow Surveys</title>
<link rel="stylesheet" href="https://fonts.googleapis.com/css2?family=Almendra:wght@700&family=Hind:wght@400;600&display=swap">
<style>
  :root {
    --card-sky: #cfe9f7;
    --card-white: #ffffff;
    --title-red: #d0103a;
    --title-shadow: rgba(90, 0, 20, 0.35);
    --ink: #111111;
    --art-magenta: #d6237e;
    --art-blue: #2a9ad8;
    --art-orange: #f39a1b;
    --art-yellow: #f7c51e;
    --art-green: #5bb84a;
  }

  * { margin: 0; padding: 0; box-sizing: border-box; }

  html, body {
    width: 900px;
    height: 1200px;
    overflow: hidden;
    background: var(--card-white);
  }

  .greeting-card {
    position: relative;
    width: 900px;
    height: 1200px;
    overflow: hidden;
    background:
      radial-gradient(ellipse 620px 700px at 620px 620px, var(--card-white) 35%, rgba(255,255,255,0) 100%),
      linear-gradient(160deg, var(--card-sky) 0%, #e6f4fb 45%, var(--card-sky) 100%);
  }

  .festive-art {
    position: absolute;
    left: 0;
    top: 0;
    width: 900px;
    height: 1200px;
  }

  .season-title {
    position: absolute;
    left: 40px;
    top: 40px;
    width: 380px;
    text-align: center;
    font-family: "Almendra", Georgia, serif;
    font-weight: 700;
    color: var(--title-red);
    text-shadow: 2px 3px 3px var(--title-shadow);
    line-height: 1.12;
  }

  .season-title .title-line {
    display: block;
    font-size: 60px;
    white-space: nowrap;
  }

  .season-title .title-joiner {
    display: block;
    font-size: 28px;
    margin: 4px 0 2px;
  }

  .season-message {
    position: absolute;
    left: 390px;
    top: 790px;
    width: 440px;
    text-align: center;
    font-family: "Hind", Arial, sans-serif;
    font-weight: 400;
    font-size: 35px;
    line-height: 46px;
    color: var(--ink);
  }

  .company-block {
    position: absolute;
    left: 40px;
    top: 985px;
    width: 260px;
    text-align: center;
    font-family: "Hind", Arial, sans-serif;
    color: var(--ink);
  }

  .company-name {
    font-family: "Hind", Arial, sans-serif;
    font-weight: 600;
    color: var(--ink);
    line-height: 1;
  }

  .company-name .name-main {
    display: block;
    font-size: 52px;
    letter-spacing: 5px;
  }

  .company-name .name-sub {
    display: block;
    font-size: 24px;
    letter-spacing: 10px;
    margin-top: 10px;
  }

  .company-established {
    margin-top: 22px;
    font-size: 19px;
    font-weight: 400;
  }

  .company-licence {
    font-size: 19px;
    font-weight: 600;
    margin-top: 2px;
  }

  .office-hours {
    position: absolute;
    left: 350px;
    top: 1096px;
    width: 520px;
    text-align: center;
    font-family: "Hind", Arial, sans-serif;
    font-size: 18px;
    line-height: 27px;
    color: var(--ink);
    white-space: nowrap;
  }
</style>
</head>
<body>
  <main class="greeting-card">

    <svg class="festive-art" viewBox="0 0 900 1200" role="img"
         aria-label="Colourful illustration: leaping kangaroos, a bursting trail of coloured bubbles and flames, boomerangs, flying birds and tumbling cubes sweeping from lower left to upper right">
      <defs>
        <linearGradient id="art-sweep" x1="0" y1="1" x2="1" y2="0">
          <stop offset="0" stop-color="var(--art-green)" stop-opacity="0.75"/>
          <stop offset="0.3" stop-color="var(--art-orange)" stop-opacity="0.8"/>
          <stop offset="0.55" stop-color="var(--art-magenta)" stop-opacity="0.75"/>
          <stop offset="0.8" stop-color="var(--art-blue)" stop-opacity="0.6"/>
          <stop offset="1" stop-color="var(--art-yellow)" stop-opacity="0.35"/>
        </linearGradient>
        <filter id="art-soften" x="-20%" y="-20%" width="140%" height="140%">
          <feGaussianBlur stdDeviation="28"/>
        </filter>
      </defs>
      <ellipse class="art-area" cx="560" cy="560" rx="470" ry="150"
               transform="rotate(-52 560 560)"
               fill="url(#art-sweep)" filter="url(#art-soften)"/>
    </svg>

    <h1 class="season-title">
      <span class="title-line">SEASON'S</span>
      <span class="title-line">GREETINGS</span>
      <span class="title-joiner">AND</span>
      <span class="title-line">HAPPY NEW</span>
      <span class="title-line">YEAR</span>
    </h1>

    <p class="season-message">
      Marlow Surveys wishes<br>
      you a safe and happy<br>
      holiday season and a<br>
      successful new year in 2013
    </p>

    <section class="company-block">
      <div class="company-name">
        <span class="name-main">MARLOW</span>
        <span class="name-sub">SURVEYS</span>
      </div>
      <p class="company-established">Established 1972</p>
      <p class="company-licence">Licensed Land Surveyors</p>
    </section>

    <p class="office-hours">
      Our office will close from 12 noon, Friday 21 December 2012<br>
      and will re-open at 9.00 am, Monday 07 January 2013.
    </p>

  </main>
</body>
</html>
```